Business card to be used as a flyer

This business card should do the trick of a full scale flyer , so basicaly from the business card itself we only keep the size and remove the clasical name , position , company name (etc).
This business cards should be , like said above, used as promo tool, being gived to different girls . So base one : the design is girls oriented.
Colors : black background . We will use gold (color) folio for the text.
Attached you have our logo, but this should not be a proiminent part of the design . You can use only the cat head instead.
Target Market(s)
Girls / Women
Contact Information for Business Card
> black background , gold / folio text and elements
> cat head from the logo in a creative way do be displayed
> proieminent text "your path to success starts here"
> contact details phone and website .
www.velmastrand.ro (website) and 0742163958 (phone)

```html
<!DOCTYPE html>
<html lang="en">
<head>
<meta charset="utf-8">
<title>Velma Strand studio – promo card</title>
<link rel="stylesheet" href="https://fonts.googleapis.com/css2?family=Bebas+Neue&family=Roboto:wght@400;500&display=swap">
<style>
  :root {
    --stage: #a3a3a3;
    --card-black: #171717;
    --band-black: #1e1e1e;
    --gold: #d6b64c;
    --gold-light: #f7e79a;
    --gold-mid: #c6a541;
    --gold-deep: #b8963a;
  }
  * { margin: 0; padding: 0; box-sizing: border-box; }
  html, body { width: 1200px; height: 1200px; overflow: hidden; }
  body {
    background: var(--stage);
    position: relative;
    font-family: "Roboto", Arial, sans-serif;
  }
  .card {
    position: absolute;
    top: 303px;
    width: 369px;
    height: 594px;
    overflow: hidden;
    background: var(--card-black);
  }
  .card--front { left: 201px; }
  .card--back { left: 599px; width: 365px; }

  .front-artwork {
    position: absolute;
    inset: 0;
    background: linear-gradient(180deg, var(--gold-light) 0%, #e6cf77 22%, var(--gold-deep) 55%, var(--gold-mid) 100%);
  }
  .front-chevron, .back-chevron {
    position: absolute;
    left: 0; top: 0;
    width: 100%; height: 100%;
  }

  .brand {
    position: absolute;
    left: 0; right: 0;
    text-align: center;
    color: var(--gold);
    font-family: "Roboto", Arial, sans-serif;
    font-weight: 500;
    line-height: 1;
  }
  .brand__name { display: block; font-size: 30px; letter-spacing: 2px; }
  .brand__studio { display: block; font-size: 18px; margin-top: 6px; padding-left: 120px; }
  .card--front .brand { top: 488px; }
  .card--back .brand { top: 106px; }

  .tagline {
    position: absolute;
    top: 278px;
    left: 0; right: 0;
    text-align: center;
    font-family: "Bebas Neue", Impact, sans-serif;
    color: var(--gold);
    font-size: 42px;
    line-height: 49px;
  }

  .contact-icon {
    position: absolute;
    left: 50%;
    width: 48px; height: 48px;
    margin-left: -24px;
  }
  .contact-icon--phone { top: 385px; }
  .contact-icon--web { top: 479px; }

  .contact-text {
    position: absolute;
    left: 0; right: 0;
    text-align: center;
    color: var(--gold);
    font-size: 24px;
    font-weight: 400;
    line-height: 1;
  }
  .contact-text--phone { top: 443px; }
  .contact-text--web { top: 532px; font-size: 23px; }
</style>
</head>
<body>

  <section class="card card--front">
    <div class="front-artwork" role="img" aria-label="Gold foil pattern of repeating cat outlines"></div>
    <svg class="front-chevron" viewBox="0 0 369 594" preserveAspectRatio="none" aria-hidden="true">
      <polygon points="0,436 47,436 184,345 324,436 369,436 369,594 0,594" fill="#1c1c1c"/>
    </svg>
    <div class="brand">
      <span class="brand__name">VELMA STRAND</span>
      <span class="brand__studio">studio</span>
    </div>
  </section>

  <section class="card card--back">
    <svg class="back-chevron" viewBox="0 0 365 594" preserveAspectRatio="none" aria-hidden="true">
      <polygon points="0,0 365,0 365,163 317,163 183,251 48,163 0,163" fill="var(--band-black)"/>
    </svg>
    <div class="brand">
      <span class="brand__name">VELMA STRAND</span>
      <span class="brand__studio">studio</span>
    </div>

    <h1 class="tagline">Your path to<br>success starts here</h1>

    <svg class="contact-icon contact-icon--phone" viewBox="0 0 48 48" aria-hidden="true">
      <circle cx="24" cy="24" r="22.5" fill="none" stroke="var(--gold)" stroke-width="2"/>
      <path d="M17 15 l4 -1 l3 6 l-3 2 q2 5 7 7 l2 -3 l6 3 l-1 4 q-3 2 -7 0 q-8 -4 -12 -12 q-2 -4 1 -6 z" fill="none" stroke="var(--gold)" stroke-width="1.8" stroke-linejoin="round"/>
      <path d="M27 15 a7 7 0 0 1 6 6 M27 11 a11 11 0 0 1 10 10" fill="none" stroke="var(--gold)" stroke-width="1.8" stroke-linecap="round"/>
    </svg>
    <div class="contact-text contact-text--phone">0742163958</div>

    <svg class="contact-icon contact-icon--web" viewBox="0 0 48 48" aria-hidden="true">
      <circle cx="24" cy="24" r="22.5" fill="none" stroke="var(--gold)" stroke-width="2"/>
      <g fill="none" stroke="var(--gold)" stroke-width="1.6">
        <circle cx="24" cy="24" r="11"/>
        <ellipse cx="24" cy="24" rx="5" ry="11"/>
        <line x1="24" y1="13" x2="24" y2="35"/>
        <line x1="13" y1="24" x2="35" y2="24"/>
        <line x1="15" y1="18.5" x2="33" y2="18.5"/>
        <line x1="15" y1="29.5" x2="33" y2="29.5"/>
      </g>
    </svg>
    <div class="contact-text contact-text--web">www.velmastrand.ro</div>
  </section>

</body>
</html>
```